The Fivefold Court Standout Image Design

We are a basketball training company with in-person and online courses and camps for players from 4th grade through college, plus coaches of all levels. We are looking for a modern design of "The Fivefold Court Standout" as the attached quick sketch shows. The seven "elements" of the complete player include: 1. Basketball IQ 2. Leadership 3. Mindset 4. Skills 5. Athleticism 6. Habits and 7. Communication
We will plan to use this design on our website, social media, emails, etc. Please see our website at vtlcourtwork.com to learn more about us and our current branding, fonts, and colors. We prefer to use the orange hex #f15d22 and blacks and dark gray. Though we have teal on our current website, we are moving away from that color so you can leave that off any designs. Thanks!
Basketball players and coaches, parents

```html
<!DOCTYPE html>
<html lang="en">
<head>
<meta charset="utf-8">
<title>The Fivefold Court Standout</title>
<link rel="stylesheet" href="https://fonts.googleapis.com/css2?family=Montserrat:wght@700;800&family=Oswald:wght@600&family=Lato:wght@900&display=swap">
<style>
  :root {
    --orange: #f15d22;
    --orange-light: #f7941d;
    --ink: #1c1c1c;
    --charcoal: #3a3a3a;
    --stage: #333436;
    --paper: #ffffff;
    --field-light: #d6d6d6;
    --field-dark: #a9a9a9;
  }
  * { margin: 0; padding: 0; box-sizing: border-box; }
  html, body { width: 1200px; height: 1200px; overflow: hidden; }
  body { background: var(--stage); position: relative; }

  .poster {
    position: absolute; left: 228px; top: 64px;
    width: 758px; height: 1070px;
    background: var(--paper);
    display: flex; flex-direction: column;
  }

  .poster-header {
    height: 130px; display: flex; align-items: center;
    justify-content: space-between; padding: 0 24px;
  }
  .brand { display: flex; align-items: center; gap: 14px; }
  .brand-dot { width: 58px; height: 58px; border-radius: 50%; background: var(--orange); }
  .brand-name {
    font-family: "Montserrat", sans-serif; font-weight: 800;
    font-size: 29px; line-height: 1.02; color: var(--ink); letter-spacing: 0.3px;
  }

  .title { text-align: center; }
  .title-kicker {
    display: flex; align-items: center; gap: 12px; justify-content: center;
    font-family: "Montserrat", sans-serif; font-weight: 800;
    font-size: 29px; color: var(--charcoal); letter-spacing: 1px;
  }
  .title-kicker::before, .title-kicker::after {
    content: ""; width: 46px; height: 3px; background: var(--orange);
  }
  .title-main {
    font-family: "Oswald", sans-serif; font-weight: 600;
    font-size: 48px; line-height: 1.05; color: var(--orange); letter-spacing: 0.5px;
  }

  .poster-field {
    height: 868px;
    background: radial-gradient(ellipse at 50% 40%, var(--field-light) 0%, #c4c4c4 55%, var(--field-dark) 100%);
  }
  .poster-field svg { display: block; }

  .element-label {
    font-family: "Lato", sans-serif; font-weight: 900; font-size: 19px;
    fill: var(--paper); letter-spacing: 0.3px;
  }
  .element-label.small { font-size: 16px; }
  .connector { stroke: #5a5a5a; stroke-width: 3; stroke-dasharray: 4 4; fill: none; }
  .badge-shape { stroke: var(--ink); stroke-width: 6; }
  .badge-icon { stroke: var(--paper); stroke-width: 2.6; fill: none; stroke-linecap: round; stroke-linejoin: round; }
  .badge-icon-fill { fill: var(--paper); }

  .poster-footer {
    height: 72px; background: var(--orange);
    display: flex; align-items: center; justify-content: center;
    font-family: "Montserrat", sans-serif; font-weight: 700;
    font-size: 30px; color: var(--paper); letter-spacing: 0.5px;
  }
</style>
</head>
<body>
<main class="poster">
  <header class="poster-header">
    <div class="brand">
      <span class="brand-dot"></span>
      <span class="brand-name">VTL<br>COURTWORK</span>
    </div>
    <div class="title">
      <div class="title-kicker">THE FIVEFOLD</div>
      <div class="title-main">COURT STANDOUT</div>
    </div>
  </header>

  <section class="poster-field">
    <svg width="758" height="868" viewBox="0 0 758 868">
      <defs>
        <linearGradient id="badgeFill" x1="0" y1="0" x2="0" y2="1">
          <stop offset="0" stop-color="#f15d22"/>
          <stop offset="1" stop-color="#f7941d"/>
        </linearGradient>
        <linearGradient id="barFill" x1="0" y1="0" x2="1" y2="0">
          <stop offset="0" stop-color="#141414"/>
          <stop offset="1" stop-color="#4a4a4a"/>
        </linearGradient>
        <linearGradient id="barFillLeft" x1="1" y1="0" x2="0" y2="0">
          <stop offset="0" stop-color="#141414"/>
          <stop offset="1" stop-color="#4a4a4a"/>
        </linearGradient>
        <radialGradient id="playerGlow" cx="0.5" cy="0.5" r="0.5">
          <stop offset="0" stop-color="#f15d22"/>
          <stop offset="0.6" stop-color="#f15d22" stop-opacity="0.85"/>
          <stop offset="1" stop-color="#f15d22" stop-opacity="0"/>
        </radialGradient>
        <path id="shield" d="M-48,-38 Q-50,-46 -40,-46 L40,-46 Q50,-46 48,-38 Q46,-4 34,16 Q20,36 0,46 Q-20,36 -34,16 Q-46,-4 -48,-38 Z"/>
      </defs>

      <g class="connectors">
        <path class="connector" d="M393,134 V304"/>
        <path class="connector" d="M259,235 H313"/>
        <path class="connector" d="M280,349 H373"/>
        <path class="connector" d="M415,320 H487"/>
        <path class="connector" d="M433,413 H497"/>
        <path class="connector" d="M505,564 H535"/>
        <path class="connector" d="M473,634 V732"/>
      </g>

      <ellipse cx="420" cy="460" rx="150" ry="310" fill="url(#playerGlow)"
               role="img" aria-label="Orange silhouette of a basketball player leaping for a one-handed dunk"/>

      <g class="labels">
        <polygon points="400,74 676,74 660,104 400,104" fill="url(#barFill)"/>
        <text class="element-label" x="463" y="97">BASKETBALL IQ</text>

        <polygon points="48,221 200,221 200,251 32,251" fill="url(#barFillLeft)"/>
        <text class="element-label" x="84" y="244">SKILLS</text>

        <polygon points="18,336 220,336 220,366 2,366" fill="url(#barFillLeft)"/>
        <text class="element-label small" x="26" y="357">COMMUNICATION</text>

        <polygon points="550,300 700,300 686,330 550,330" fill="url(#barFill)"/>
        <text class="element-label" x="590" y="323">MINDSET</text>

        <polygon points="556,396 742,396 726,426 556,426" fill="url(#barFill)"/>
        <text class="element-label" x="584" y="419">LEADERSHIP</text>

        <polygon points="596,548 736,548 720,578 596,578" fill="url(#barFill)"/>
        <text class="element-label" x="633" y="571">HABIT</text>

        <polygon points="490,770 698,770 682,800 490,800" fill="url(#barFill)"/>
        <text class="element-label" x="526" y="793">ATHLETICISM</text>
      </g>

      <!-- Basketball IQ -->
      <g transform="translate(383,90)">
        <use href="#shield" class="badge-shape" fill="url(#badgeFill)"/>
        <circle class="badge-icon" cx="0" cy="-8" r="18"/>
        <path class="badge-icon" d="M-18,-8 H18 M0,-26 V10 M-12,-21 Q-4,-8 -12,5 M12,-21 Q4,-8 12,5"/>
      </g>
      <!-- Skills -->
      <g transform="translate(217,222)">
        <use href="#shield" class="badge-shape" fill="url(#badgeFill)"/>
        <circle class="badge-icon" cx="-15" cy="-18" r="3.5"/>
        <circle class="badge-icon" cx="0" cy="-25" r="3.5"/>
        <circle class="badge-icon" cx="15" cy="-18" r="3.5"/>
        <circle class="badge-icon" cx="0" cy="-6" r="5"/>
        <path class="badge-icon" d="M-11,14 V6 Q-11,2 -6,2 H6 Q11,2 11,6 V14 M-11,4 L-18,-8 M11,4 L18,-8"/>
      </g>
      <!-- Communication -->
      <g transform="translate(233,346)">
        <use href="#shield" class="badge-shape" fill="url(#badgeFill)"/>
        <path class="badge-icon" d="M-5,-24 Q0,-28 5,-24 M-9,-28 Q0,-35 9,-28"/>
        <circle class="badge-icon-fill" cx="0" cy="-20" r="1.8"/>
        <circle class="badge-icon" cx="-10" cy="-8" r="5"/>
        <circle class="badge-icon" cx="10" cy="-8" r="5"/>
        <path class="badge-icon" d="M-19,12 V4 Q-19,0 -14,0 H-6 Q-1,0 -1,4 V12 Z M1,12 V4 Q1,0 6,0 H14 Q19,0 19,4 V12 Z"/>
      </g>
      <!-- Mindset -->
      <g transform="translate(533,296)">
        <use href="#shield" class="badge-shape" fill="url(#badgeFill)"/>
        <path class="badge-icon" d="M-8,16 V6 Q-20,-2 -16,-16 Q-10,-30 6,-28 Q20,-25 19,-10 L23,-2 L18,0 V8 H10 V16"/>
        <circle class="badge-icon" cx="2" cy="-11" r="8"/>
        <path class="badge-icon" d="M-2,-11 L1,-8 L6,-14"/>
      </g>
      <!-- Leadership -->
      <g transform="translate(540,400)">
        <use href="#shield" class="badge-shape" fill="url(#badgeFill)"/>
        <path class="badge-icon" d="M-20,14 H20 M-6,14 V4 H8 V14"/>
        <circle class="badge-icon" cx="-10" cy="-20" r="4"/>
        <path class="badge-icon" d="M-10,-15 V0 M-10,-11 L0,-18 M-10,0 L-14,10 M-10,0 L-4,4"/>
        <path class="badge-icon" d="M0,-18 L14,-26 M17,-30 L20,-33 M18,-24 L23,-24"/>
      </g>
      <!-- Habit -->
      <g transform="translate(581,548)">
        <use href="#shield" class="badge-shape" fill="url(#badgeFill)"/>
        <path class="badge-icon" d="M-16,-14 A18,18 0 1 1 -18,-2"/>
        <path class="badge-icon" d="M-22,-20 L-16,-14 L-9,-19"/>
        <path class="badge-icon" d="M0,-18 V-6 L9,0"/>
      </g>
      <!-- Athleticism -->
      <g transform="translate(473,776)">
        <use href="#shield" class="badge-shape" fill="url(#badgeFill)"/>
        <circle class="badge-icon" cx="8" cy="-24" r="4"/>
        <path class="badge-icon" d="M-12,-12 L-2,-17 L8,-14 L2,-2 L10,6 L8,16 M2,-2 L-6,6 L-18,4 M8,-14 L14,-6 L20,-8"/>
      </g>
    </svg>
  </section>

  <footer class="poster-footer">VTLCOURTWORK.COM</footer>
</main>
</body>
</html>
```